Company Brochure / Sales Sheet

We would like a brochure that we will may print out as well as forward electronically to our prospective clients.

Our clients are inventors/doctors/surgeons of medical products who need help completing their medical product, gaining approval, and then selling their product into the US market

Target Market(s)

Inventors of medical products who want to sell them in the United States

Industry/Entity Type

Medical

Font styles to use
Serif
Sans Serif

Requirements
Must have
• The word "Medical" should not receive special empahsis.
• Use the last two photos and whatever other photos that look good. You can edit and crop the photos
• Text should be easy to read
Nice to have
• We want to show that we have a lot of products.
• Sharp, clean, modern
• Minimum two pages - final product should be capable of being printed and
• forwarded electronically
• Easy to read
Should not have
• Should not be cluttered

```html
<!DOCTYPE html>
<html lang="en">
<head>
<meta charset="utf-8">
<title>Meridian Health Partners – Brochure</title>
<link rel="stylesheet" href="https://fonts.googleapis.com/css2?family=Montserrat:wght@600&family=Open+Sans:wght@400;600&family=Oswald:wght@500&display=swap">
<style>
:root{
  --red:#d21f34;
  --dark:#2b2b2d;
  --ink:#2e2e30;
  --paper:#ffffff;
  --mist:#ececee;
  --stage:#f2f2f2;
}
*{margin:0;padding:0;box-sizing:border-box}
html,body{width:1200px;height:1200px;overflow:hidden;background:var(--stage)}
.canvas{position:relative;width:1200px;height:1200px}
.page{position:absolute;top:255px;width:490px;height:690px;background:var(--paper);overflow:hidden}
.page--front{left:55px}
.page--back{left:655px;background:linear-gradient(160deg,#f7f7f8 0%,var(--mist) 100%)}
.page svg.bands{position:absolute;left:0;top:0;width:490px;height:690px}
.photo{position:absolute}
.brand{position:absolute;text-align:center;font-family:"Montserrat",sans-serif;font-weight:600;color:var(--dark)}
.brand__mark{display:block;margin:0 auto 6px;width:36px;height:36px;border-radius:50%;background:var(--red)}
.brand__name{font-size:15px;line-height:1.2;letter-spacing:.3px}
.brand__sub{font-size:10px;letter-spacing:8px;margin-top:2px}
.heading{font-family:"Oswald",sans-serif;font-weight:500;color:var(--red);text-transform:uppercase;letter-spacing:.2px}
.body-copy{font-family:"Open Sans",sans-serif;font-size:8px;line-height:1.38;color:var(--ink)}
.body-copy p{margin-bottom:10px}
.about{position:absolute;left:42px;top:275px;width:408px}
.about .heading{font-size:19px;margin-bottom:10px}
.about .body-copy{text-align:justify;font-size:7.6px;line-height:1.4}
.about .body-copy p{margin-bottom:9px}
.about p.narrow{width:280px}
.call{position:absolute;font-family:"Oswald",sans-serif;font-weight:500;color:var(--red);white-space:nowrap}
.call--front{left:42px;top:545px;font-size:27px}
.call--back{left:33px;top:537px;font-size:25px}
.url{position:absolute;left:40px;top:653px;font-family:"Open Sans",sans-serif;font-weight:600;font-size:11px;letter-spacing:1.6px;color:#fff}
.service{position:absolute;left:36px;width:320px;display:flex;gap:12px}
.service__icon{flex:0 0 33px;width:33px;height:33px}
.service .heading{font-size:14px;margin:3px 0 8px}
.service .body-copy p{margin-bottom:9px}
</style>
</head>
<body>
<main class="canvas">

  <section class="page page--front">
    <svg class="bands" viewBox="0 0 490 690" aria-hidden="true">
      <path d="M0 222 C120 255 330 230 490 110 L490 128 C330 245 130 268 0 236 Z" fill="var(--dark)"/>
      <path d="M0 232 C130 262 330 240 490 122 L490 175 C340 270 130 272 0 250 Z" fill="var(--red)"/>
      <path d="M0 620 L320 590 L490 528 L490 548 L330 606 L0 632 Z" fill="var(--dark)"/>
      <path d="M0 630 L330 604 L490 546 L490 690 L0 690 Z" fill="var(--red)"/>
    </svg>

    <div class="photo" role="img" aria-label="Tablet showing medical scans with a stethoscope draped over it"
         style="left:30px;top:18px;width:235px;height:185px;background:radial-gradient(circle at 45% 40%,#5fb7cf 0%,#2c5f80 45%,#dfe6ec 75%,#fff 100%);border-radius:10px"></div>

    <div class="photo" style="left:300px;top:140px;width:130px;height:130px;transform:rotate(-22deg);background:var(--red)"></div>
    <div class="photo" role="img" aria-label="Close-up of a white surgical mask on blue fabric"
         style="left:290px;top:135px;width:130px;height:130px;transform:rotate(-18deg);border:4px solid #fff;background:radial-gradient(ellipse at 50% 55%,#f2f2f2 0%,#d9dde3 30%,#3656a4 55%,#26428a 100%)"></div>

    <div class="brand" style="left:250px;top:22px;width:200px">
      <span class="brand__mark"></span>
      <div class="brand__name">MERIDIAN HEALTH</div>
      <div class="brand__sub">PARTNERS</div>
    </div>

    <article class="about">
      <h2 class="heading">About Us</h2>
      <div class="body-copy">
        <p>We are a network of medical distribution professionals including physicians and surgeons, regulatory and coding experts, patent and trademark lawyers, international fulfillment experts, marketing and advertising professionals, and business strategists all working together in the distribution of promising new medical products. We handle all aspects of new surgical product sales, marketing, and distribution.</p>
        <p>Our company was founded in Milford, Delaware, with distribution locations and support associates and affiliates located throughout the US. We have extensive experience with medical product development, intellectual property, and regulatory and compliances issues.</p>
        <p>We partner with medical innovators by providing strategic support with intellectual property and regulatory approval, reimbursement coding, marketing, selling and distributing state of the art medical products. Our clients include highly creative medical companies with strong management teams and consumer-driven growth perspectives.</p>
        <p class="narrow">Our products are uniquely positioned in an evolving health sector to offer benefits to patients, healthcare institutions, medical professionals, insurance companies and governmental agencies. Our evidence-based technologies reduce overall healthcare expenses and empower physicians and surgeons to provide improved practices and standards of care.</p>
      </div>
    </article>

    <div class="call call--front">CALL: (302) 555-0148</div>

    <div class="photo" role="img" aria-label="Doctor in a white coat with stethoscope holding a clipboard"
         style="left:332px;top:465px;width:148px;height:225px;background:linear-gradient(180deg,#e8d7c6 0%,#f4f6f8 30%,#cfe0f0 55%,#8f8a80 100%)"></div>

    <div class="url">www.meridianhealthpartners.com</div>
  </section>

  <section class="page page--back">
    <svg class="bands" viewBox="0 0 490 690" aria-hidden="true">
      <polygon points="0,0 180,0 60,140" fill="#fff" opacity=".45"/>
      <polygon points="0,300 120,420 0,520" fill="#fff" opacity=".4"/>
      <path d="M258 0 L300 0 C420 140 455 340 432 560 L410 565 C430 340 390 140 258 0 Z" fill="var(--dark)"/>
      <path d="M285 0 L490 0 L490 545 L440 560 C465 340 420 140 285 0 Z" fill="var(--red)"/>
      <path d="M0 620 L300 590 L490 528 L490 548 L310 606 L0 632 Z" fill="var(--dark)"/>
      <path d="M0 630 L310 604 L490 546 L490 690 L0 690 Z" fill="var(--red)"/>
    </svg>

    <div class="brand" style="left:45px;top:40px;width:220px">
      <span class="brand__mark"></span>
      <div class="brand__name">MERIDIAN HEALTH</div>
      <div class="brand__sub">PARTNERS</div>
    </div>

    <div class="service" style="top:158px">
      <svg class="service__icon" viewBox="0 0 33 33" aria-hidden="true"><circle cx="16.5" cy="16.5" r="16.5" fill="var(--red)"/><path d="M13.5 8h6v5.5H25v6h-5.5V25h-6v-5.5H8v-6h5.5Z" fill="#fff"/></svg>
      <div>
        <h3 class="heading">Medical Products</h3>
        <div class="body-copy">
          <p>We specialize in the distribution of next generation medical products including customized surgical instruments and kits, monitoring and diagnostic devices, advanced wound care products and innovative acute care disposables.</p>
          <p>Our medical products represent breakthroughs in medical technology, saving lives, reducing health care costs, improving patient lifestyles.</p>
        </div>
      </div>
    </div>

    <div class="service" style="top:293px">
      <svg class="service__icon" viewBox="0 0 33 33" aria-hidden="true"><circle cx="16.5" cy="16.5" r="16.5" fill="var(--red)"/><path d="M8 24V15h3v-3h3v3h2v-5h3v5h2v-3h3v12Z" fill="#fff"/></svg>
      <div>
        <h3 class="heading">Intellectual Property and Branding</h3>
        <div class="body-copy" style="text-align:justify">
          <p>We help our partners get the trademarks and patent claim approvals they need and deserve and at a reasonable price. Our team of patent attorneys and agents is effective and affordable and has gained over 300 client patent approvals. We help our clients brand and position their products for successful product launches and introductions to the US market.</p>
        </div>
      </div>
    </div>

    <div class="service" style="top:402px;width:280px">
      <svg class="service__icon" viewBox="0 0 33 33" aria-hidden="true"><circle cx="16.5" cy="16.5" r="16.5" fill="var(--red)"/><path d="M8 10l7 6.5-7 6.5M16 10l7 6.5-7 6.5" fill="none" stroke="#fff" stroke-width="3.2" stroke-linejoin="round"/></svg>
      <div>
        <h3 class="heading">Regulatory Issues</h3>
        <div class="body-copy">
          <p>We provide comprehensive services support for global physician inventors who are seeking to distribute their medical products within the United States. We assist in navigating the unique aspects of the US medical market – including FDA compliance and device returns, US Customs, and reimbursement coding.</p>
        </div>
      </div>
    </div>

    <div class="call call--back">CALL: (302) 555-0148</div>

    <div class="photo" style="left:332px;top:510px;width:120px;height:120px;transform:rotate(45deg);background:var(--dark)"></div>
    <div class="photo" role="img" aria-label="Blue surgical mask with white ties"
         style="left:322px;top:498px;width:120px;height:120px;transform:rotate(45deg);border:4px solid #fff;background:linear-gradient(135deg,#e9ecef 0%,#cfd6df 30%,#3a5aa8 50%,#26428a 100%)"></div>

    <div class="url">www.meridianhealthpartners.com</div>
  </section>

</main>
</body>
</html>
```